FeedBack Solution Provider - Web Redesign

Lumora Website design request We are looking for a redesign for our website www.lumora-example.com 1 web page site +2, we are providing feedback collection solution through tablet devices and online iframes, sms, emails.. we want to optimize our website design to communicate our products values better (increase your customer satisfaction – get to know your customers – happy customers – increased business performance)Also to give visitors more insight to our different products (channels) layouts.A pricing section for minimum of 2 packages (SAAS) that include many features and hardware addons as a selection field. 3rd package clients to design their own packages through selection of components and addons no price needed in this feature (request quote).1 Web Page Sections will go as follows:1. Header2. Slider3. Why LuMora (points and values)4. Features 5. Packages (pricing based on SaaS and hardware as addon)6. Impact of using RaiBack7. Clients Testimonies8. Contact9. Footer +2 Web Pages Adding to additional web pages by copying the following sections with different content (will be hidden for the moment)1. Slider2. Features 3. Packages (pricing based on SaaS and hardware as addon)4. Impact of using RaiBack5. Clients TestimoniesHints: https://velkintor42.sitebuilder-example.com/lumora www.lumora-example.com

Target Market(s)

B2B

Industry/Entity Type

SaaS

Number of Pages Required

1 page

Font styles to use
Sans Serif

Colors

Designer to choose colors to be used in the design.

Requirements
Must have
• 1 Web Page Sections will go as follows:
• 1. Header
• 2. Slider
• 3. Why LuMora (points and values)
• 4. Features
• 5. Packages (pricing based on SaaS and hardware as addon)
• 6. Impact of using LuMora
• 7. Clients Testimonies
• 8. Contact
• 9. Footer
Nice to have
• +2 Web Pages Adding to additional web pages by copying the following sections with different content (will be hidden for the moment)
• 1. Slider
• 2. Features
• 3. Packages (pricing based on SaaS and hardware as addon)
• 4. Impact of using LuMora
• 5. Clients Testimonies

```html
<!DOCTYPE html>
<html lang="en">
<head>
<meta charset="utf-8">
<title>LuMora — Feedback Solutions</title>
<link rel="stylesheet" href="https://fonts.googleapis.com/css2?family=Roboto:wght@300;400;500;700&display=swap">
<style>
:root{
  --blue:#1a8cf0;
  --blue-deep:#0b6fe0;
  --blue-text:#1f7fe6;
  --orange:#f7871f;
  --ink:#222a36;
  --muted:#8a93a3;
  --page:#f3f5fa;
  --card:#ffffff;
  --line:#e3e7ee;
  --band:#eceff5;
  --dark:#1e2b4a;
}
*{box-sizing:border-box;margin:0;padding:0}
html,body{width:1200px;height:4706px;overflow:hidden}
body{position:relative;background:var(--page);font-family:"Roboto",sans-serif;color:var(--ink)}
.abs{position:absolute}
.hero-bg{position:absolute;left:0;top:0}
.brand{position:absolute;left:28px;top:30px;display:flex;align-items:center;gap:8px;color:#fff;font-weight:500;font-size:18px}
.brand .dot{width:22px;height:22px;border:2px solid #fff;border-radius:50%}
.nav{position:absolute;left:812px;top:44px;display:flex;gap:34px;font-size:10px;color:#d9ecff}
.nav .active{color:#fff;font-weight:700}
.nav .lang{border:1px solid #fff;padding:1px 8px;color:#fff;margin-top:-2px}
.hero-title{left:108px;top:210px;font-size:42px;font-weight:400;color:#fff}
.hero-copy{left:108px;top:286px;width:452px;font-size:13.5px;line-height:22.5px;color:#e5f1ff;font-weight:300}
.btn{position:absolute;display:flex;align-items:center;justify-content:center;color:#fff;font-size:9px;font-weight:700;letter-spacing:.5px;text-transform:uppercase}
.btn-orange{background:var(--orange)}
.btn-blue{background:var(--blue)}
.btn-gray{background:#c9ced6}
.hero-photo{left:668px;top:197px;width:479px;height:342px;background:linear-gradient(135deg,#5d6f86,#c7d3df 55%,#8fa3b8)}
.section-title{position:absolute;left:0;width:1200px;text-align:center;font-weight:700}
.sub{position:absolute;left:0;width:1200px;text-align:center;font-size:16px;color:var(--ink)}
.wheel{left:316px;top:718px;width:580px;height:370px;border-radius:14px;background:radial-gradient(circle at 50% 50%,#ffffff 0,#cfe6fc 9%,#2a95f3 10%,#1886ee 60%,#0f74e3)}
.feature-card{position:absolute;width:292px;height:64px;background:#fff;box-shadow:0 6px 18px rgba(30,60,120,.1);border-radius:3px;padding:12px 14px 0 64px}
.feature-card .ic{position:absolute;left:16px;top:14px;width:34px;height:34px;border-radius:50%}
.feature-card h4{font-size:7.5px;color:var(--blue-text);font-weight:700;margin-bottom:4px}
.feature-card p{font-size:7px;line-height:10px;color:var(--ink)}
.video{left:46px;top:1278px;width:535px;height:360px;border-radius:14px;background:linear-gradient(180deg,#3a3e56,#15172a);border:8px solid #1a1c28}
.video-base{left:0;top:1640px;width:640px;height:8px;background:var(--blue);border-radius:0 0 8px 8px}
.kicker{font-size:17px;line-height:27px;color:var(--orange)}
.body-lg{font-size:15px;line-height:26px;color:var(--ink)}
.body-sm{font-size:9px;line-height:12px;color:var(--muted)}
.devices{left:566px;top:1826px;width:511px;height:365px;border-radius:18px;background:linear-gradient(135deg,#e9edf4 0,#dfe5ee 40%,#c9d1dd 75%,#e7ebf2)}
.chat{position:absolute;width:286px;height:48px;background:#fff;box-shadow:0 6px 16px rgba(30,60,120,.1);padding:10px 0 0 62px;font-size:7px;color:var(--muted)}
.chat b{display:block;color:var(--ink);font-size:7px;margin-bottom:2px}
.chat .av{position:absolute;left:18px;top:9px;width:30px;height:30px;border-radius:50%;background:#dfe5ef}
.chat span{color:var(--blue-text)}
.doc{position:absolute;background:#fff;box-shadow:0 6px 16px rgba(30,60,120,.1)}
.doc i{position:absolute;left:50%;transform:translateX(-50%);top:14px;width:18px;height:18px}
.pkg{position:absolute;background:#fff;box-shadow:0 8px 24px rgba(30,60,120,.08)}
.pkg h5{position:absolute;left:26px;top:24px;font-size:11px;font-weight:700}
.pkg .plus{position:absolute;right:18px;top:18px;width:28px;height:28px;border-radius:50%;background:#e8ebf1;color:var(--muted);text-align:center;line-height:27px;font-size:18px}
.price{position:absolute;font-size:32px;font-weight:500}
.price sup{font-size:10px;vertical-align:top;margin-right:6px}
.list{position:absolute;list-style:none}
.list li{height:42px;font-size:11px;display:flex;align-items:flex-start;gap:18px}
.tick{width:12px;height:10px}
.box{width:18px;height:18px;border:1.5px solid #777;display:inline-block}
.clients{left:0;top:3333px;width:1200px;height:273px;background:var(--band)}
.client{position:absolute;top:3462px;font-size:22px;font-weight:500;color:#3b4250;display:flex;align-items:center;gap:10px}
.client .mk{width:18px;height:18px;background:#3b4250;border-radius:50%}
.faded{opacity:.25}
.t-card{position:absolute;background:#fff;box-shadow:0 10px 30px rgba(30,60,120,.08)}
.map{left:0;top:4081px;width:1200px;height:400px;background:linear-gradient(160deg,#eef1f3 0,#e2e7ec 35%,#d7dee6 60%,#e9edf1 80%,#dde3e9)}
.footer{left:0;top:4474px;width:1200px;height:232px;background:linear-gradient(90deg,#1790f2,#0c72e2)}
.contact{left:27px;top:4227px;width:384px;height:411px;background:#fff;box-shadow:0 10px 30px rgba(30,60,120,.15)}
.field{position:absolute;left:31px;width:322px;height:27px;background:#f1f3f7;font-size:9px;color:var(--muted);padding:8px 8px}
.f-info{left:730px;top:4562px;font-size:9px;line-height:20px;color:#fff}
.social{position:absolute;top:4575px;width:24px;height:24px;border-radius:50%;border:1px solid rgba(255,255,255,.7)}
.copy{left:0;top:4680px;width:1200px;text-align:center;font-size:9px;color:#e5f1ff}
</style>
</head>
<body>

<svg class="hero-bg" width="1200" height="1200" viewBox="0 0 1200 1200" aria-hidden="true">
  <defs><linearGradient id="hg" x1="0" y1="0" x2="1" y2="1"><stop offset="0" stop-color="#1a8cf0"/><stop offset="1" stop-color="#0d70e2"/></linearGradient></defs>
  <path d="M0 0H1200V1120C1120 900 960 650 760 600C560 560 300 620 0 694Z" fill="url(#hg)"/>
  <rect x="849" y="118" width="351" height="38" fill="#ffffff" opacity=".9"/>
  <rect x="748" y="156" width="452" height="300" fill="#ffffff" opacity=".12"/>
</svg>

<header>
  <div class="brand"><span class="dot"></span>LuMora</div>
  <nav class="nav"><span class="active">HOME</span><span>About Us</span><span>Features</span><span>Pricing</span><span>Contact</span><span class="lang">عربي</span></nav>
</header>

<section class="slider">
  <h1 class="abs hero-title">LuMora</h1>
  <p class="abs hero-copy">Lorem Ipsum is simply dummy text of the printing and typesetting industry. Lorem Ipsum has been the industry's standard dummy text ever since the 1500s, when an unknown printer took a galley of type and scrambled it to make a type specimen book.It has survived not only five centuries, but also the leap into electronic typesetting, remaining essentially unchanged. It was in the release of Letraset.</p>
  <a class="btn btn-orange" style="left:108px;top:467px;width:115px;height:28px">Sign up</a>
  <div class="abs hero-photo" role="img" aria-label="Photo of two colleagues smiling at a computer screen"></div>
</section>

<section class="why">
  <h2 class="section-title" style="top:656px;font-size:21px;font-weight:500">A flexible solution for business</h2>
  <div class="abs wheel" role="img" aria-label="Illustration of a tablet showing LuMora feedback channels arranged around a central hub"></div>
  <svg class="abs" style="left:0;top:1040px" width="1200" height="860" aria-hidden="true">
    <circle cx="600" cy="420" r="600" fill="none" stroke="#4aa3f5" stroke-width="2" stroke-dasharray="2 8"/>
  </svg>
</section>

<section class="features">
  <h2 class="section-title" style="top:1170px;font-size:22px;color:var(--blue-text);font-weight:500">Admin Panel Features</h2>
  <p class="sub" style="top:1205px">One of the best service provider in market</p>
  <div class="abs video" role="img" aria-label="Product video showing customers giving feedback"></div>
  <svg class="abs" style="left:274px;top:1418px" width="80" height="80" aria-label="Play"><circle cx="40" cy="40" r="22" fill="#fff" opacity=".85"/><path d="M34 29L52 40L34 51Z" fill="#1e2b4a"/></svg>
  <div class="abs video-base"></div>
  <div class="feature-card" style="left:708px;top:1287px"><span class="ic" style="background:#dcecff"></span><h4>REAL TIME DATA</h4><p>respondents data is reflected on the Dashboard<br>upon submission of evaluation</p></div>
  <div class="feature-card" style="left:737px;top:1393px"><span class="ic" style="background:#f1e4ff"></span><h4>ACCURATE EVALUATION</h4><p>Supports multi-branches, departments, events,<br>staff, service or products evaluations</p></div>
  <div class="feature-card" style="left:733px;top:1499px"><span class="ic" style="background:#ffeedd"></span><h4>PERSONALIZED &amp; COMPATIBILITY</h4><p>branded interface (logo, interface, colors, picture)<br>Multilanguage and supports all android devices</p></div>
  <div class="feature-card" style="left:708px;top:1605px"><span class="ic" style="background:#ffe7d6"></span><h4>DASHBOARD</h4><p>Monitor performance through on-demand reports<br>and get preset notification</p></div>

  <p class="abs kicker" style="left:144px;top:1892px">Feedback Kiosks &amp;<br>tablets features</p>
  <p class="abs body-lg" style="left:144px;top:1960px">If you are in the market<br>for a computer, there are<br>a number of factors to</p>
  <p class="abs body-sm" style="left:144px;top:2062px">If you are in the market for a computer,<br>there are a number of factors to consider</p>
  <a class="btn btn-orange" style="left:144px;top:2109px;width:101px;height:22px;font-size:7px">Explore plans</a>
  <div class="abs devices" role="img" aria-label="Illustration of a smartphone and a tablet kiosk showing rating faces"></div>

  <svg class="abs" style="left:90px;top:2230px" width="520" height="360" aria-hidden="true"><path d="M80 60C150 -10 330 10 400 90C470 170 430 300 300 330C170 360 40 300 20 200C10 140 40 100 80 60Z" fill="#e6eaf2"/></svg>
  <div class="chat" style="left:161px;top:2301px"><span class="av"></span><b>Nadia Fairbrook</b>@owen: We are ready with the <span>latest report</span></div>
  <div class="chat" style="left:104px;top:2405px"><span class="av"></span><b>Owen Kettleby</b><span>@nadia</span>: Could you share the <span>team</span> please?</div>
  <div class="chat" style="left:161px;top:2511px"><span class="av"></span><b>Nadia Fairbrook</b><span>@owen</span>: Sure, no problem</div>
  <div class="doc" style="left:502px;top:2341px;width:68px;height:88px"><i style="background:var(--orange)"></i></div>
  <div class="doc" style="left:469px;top:2456px;width:46px;height:64px"><i style="background:#1e3a8a;width:14px;height:14px;top:10px"></i></div>
  <p class="abs" style="left:771px;top:2340px;font-size:17px;color:var(--blue-text)">SMS, QR &amp; API's features.</p>
  <p class="abs body-lg" style="left:771px;top:2378px">If you are in the market<br>for a computer, there are<br>a number of factors to</p>
  <a class="btn btn-blue" style="left:772px;top:2489px;width:101px;height:22px;font-size:7px">Explore plans</a>
</section>

<section class="packages">
  <h2 class="section-title" style="top:2668px;font-size:22px">Our Packages</h2>
  <p class="sub" style="top:2700px">If you are in the market</p>

  <div class="pkg" style="left:150px;top:2766px;width:281px;height:512px">
    <h5>Free Package</h5><span class="plus">+</span>
    <div class="price" style="left:90px;top:96px"><sup>$</sup>39.99</div>
    <ul class="list" style="left:66px;top:186px">
      <li><svg class="tick" viewBox="0 0 12 10"><path d="M1 5l3.5 3.5L11 1" fill="none" stroke="#1f7fe6" stroke-width="1.6"/></svg>Lorem ipsum</li>
      <li><svg class="tick" viewBox="0 0 12 10"><path d="M1 5l3.5 3.5L11 1" fill="none" stroke="#1f7fe6" stroke-width="1.6"/></svg>Dolor sit amet</li>
      <li><svg class="tick" viewBox="0 0 12 10"><path d="M1 5l3.5 3.5L11 1" fill="none" stroke="#1f7fe6" stroke-width="1.6"/></svg>Consectetur adipisicin</li>
      <li><svg class="tick" viewBox="0 0 12 10"><path d="M1 5l3.5 3.5L11 1" fill="none" stroke="#1f7fe6" stroke-width="1.6"/></svg>Sed do eiusmo</li>
      <li><svg class="tick" viewBox="0 0 12 10"><path d="M1 5l3.5 3.5L11 1" fill="none" stroke="#1f7fe6" stroke-width="1.6"/></svg>Tempor incididunt</li>
    </ul>
    <a class="btn btn-gray" style="left:90px;top:438px;width:100px;height:22px;font-size:7px">Subscribe</a>
  </div>

  <div class="pkg" style="left:456px;top:2766px;width:282px;height:512px">
    <h5 style="color:var(--orange)">Entry Package</h5><span class="plus" style="background:#fde9d6;color:var(--orange)">+</span>
    <div class="price" style="left:82px;top:74px;color:var(--orange)"><sup>$</sup>79.99</div>
    <ul class="list" style="left:66px;top:152px;color:var(--orange)">
      <li><svg class="tick" viewBox="0 0 12 10"><path d="M1 5l3.5 3.5L11 1" fill="none" stroke="#f7871f" stroke-width="1.6"/></svg>Lorem ipsum</li>
      <li><svg class="tick" viewBox="0 0 12 10"><path d="M1 5l3.5 3.5L11 1" fill="none" stroke="#f7871f" stroke-width="1.6"/></svg>Dolor sit amet</li>
      <li><svg class="tick" viewBox="0 0 12 10"><path d="M1 5l3.5 3.5L11 1" fill="none" stroke="#f7871f" stroke-width="1.6"/></svg>Consectetur adipisicin</li>
      <li><svg class="tick" viewBox="0 0 12 10"><path d="M1 5l3.5 3.5L11 1" fill="none" stroke="#f7871f" stroke-width="1.6"/></svg>Sed do eiusmo</li>
      <li><svg class="tick" viewBox="0 0 12 10"><path d="M1 5l3.5 3.5L11 1" fill="none" stroke="#f7871f" stroke-width="1.6"/></svg>Tempor incididunt</li>
      <li><svg class="tick" viewBox="0 0 12 10"><path d="M1 5l3.5 3.5L11 1" fill="none" stroke="#f7871f" stroke-width="1.6"/></svg>Sed do eiusmo</li>
      <li><svg class="tick" viewBox="0 0 12 10"><path d="M1 5l3.5 3.5L11 1" fill="none" stroke="#f7871f" stroke-width="1.6"/></svg>Tempor incididunt</li>
    </ul>
    <a class="btn btn-orange" style="left:92px;top:460px;width:100px;height:22px;font-size:7px">Subscribe</a>
  </div>

  <div class="pkg" style="left:760px;top:2761px;width:295px;height:526px;border:3px solid var(--blue)">
    <h5 style="color:var(--blue-text);top:28px">User Custom Package</h5>
    <span class="abs" style="right:24px;top:26px;font-size:14px;color:#555">⋮</span>
    <ul class="list" style="left:40px;top:74px;color:var(--blue-text)">
      <li style="align-items:center"><svg width="18" height="18" viewBox="0 0 18 18"><rect x=".75" y=".75" width="16.5" height="16.5" fill="none" stroke="#1f7fe6" stroke-width="1.5"/><path d="M4 9l3.5 3.5L14 5" fill="none" stroke="#1f7fe6" stroke-width="1.5"/></svg>Lorem ipsum</li>
      <li style="align-items:center"><svg width="18" height="18" viewBox="0 0 18 18"><rect x=".75" y=".75" width="16.5" height="16.5" fill="none" stroke="#1f7fe6" stroke-width="1.5"/><path d="M4 9l3.5 3.5L14 5" fill="none" stroke="#1f7fe6" stroke-width="1.5"/></svg>Dolor sit amet</li>
      <li style="align-items:center"><svg width="18" height="18" viewBox="0 0 18 18"><rect x=".75" y=".75" width="16.5" height="16.5" fill="none" stroke="#1f7fe6" stroke-width="1.5"/><path d="M4 9l3.5 3.5L14 5" fill="none" stroke="#1f7fe6" stroke-width="1.5"/></svg>Consectetur adipisicin</li>
      <li style="align-items:center"><svg width="18" height="18" viewBox="0 0 18 18"><rect x=".75" y=".75" width="16.5" height="16.5" fill="none" stroke="#1f7fe6" stroke-width="1.5"/><path d="M4 9l3.5 3.5L14 5" fill="none" stroke="#1f7fe6" stroke-width="1.5"/></svg>Sed do eiusmo</li>
      <li style="align-items:center"><svg width="18" height="18" viewBox="0 0 18 18"><rect x=".75" y=".75" width="16.5" height="16.5" fill="none" stroke="#1f7fe6" stroke-width="1.5"/><path d="M4 9l3.5 3.5L14 5" fill="none" stroke="#1f7fe6" stroke-width="1.5"/></svg>Tempor incididunt</li>
      <li style="align-items:center"><span class="box"></span>Consectetur adipisicin</li>
      <li style="align-items:center"><span class="box"></span>Sed do eiusmo</li>
    </ul>
    <span class="abs" style="left:26px;top:418px;font-size:10px;color:var(--blue-text)">TOTAL</span>
    <div class="price" style="left:164px;top:396px;color:var(--blue-text)"><sup>$</sup>79.99</div>
    <a class="btn btn-blue" style="left:90px;top:484px;width:102px;height:22px;font-size:7px">Subscribe</a>
  </div>
</section>

<section class="impact">
  <div class="abs clients"></div>
  <h2 class="section-title" style="top:3352px;font-size:22px">OUR CLIENTS</h2>
  <div class="client faded" style="left:0"><span class="mk"></span>Civic</div>
  <div class="client" style="left:155px"><span class="mk"></span>Horizon Plan</div>
  <div class="client" style="left:420px">Wellvista</div>
  <div class="client" style="left:658px;font-size:18px">Skyline Catering</div>
  <div class="client" style="left:858px"><span class="mk"></span>Northpost</div>
  <div class="client faded" style="left:1042px">Quadra</div>
</section>

<section class="testimonials">
  <h2 class="section-title" style="top:3650px;font-size:22px;color:var(--blue-text);font-weight:500">Testimonials</h2>
  <p class="sub" style="top:3684px">What People are saying</p>
  <div class="t-card" style="left:156px;top:3775px;width:120px;height:200px;opacity:.5"><p style="padding:70px 0 0 34px;font-size:9px;line-height:13px;color:#aab">Lorem Ip<br>Ipsum ha<br>unknow</p></div>
  <div class="t-card" style="left:924px;top:3775px;width:110px;height:200px;opacity:.5"><p style="padding:70px 0 0 46px;font-size:9px;line-height:13px;color:#aab">Lorem<br>when an<br>cimen</p></div>
  <div class="t-card" style="left:228px;top:3749px;width:740px;height:250px">
    <div class="abs" role="img" aria-label="Customer portrait" style="left:334px;top:12px;width:70px;height:70px;border-radius:50%;background:linear-gradient(135deg,#d8b79a,#6b7a8c)"></div>
    <p class="abs" style="left:0;width:740px;top:100px;text-align:center;font-size:11px;font-weight:500">User Name</p>
    <p class="abs" style="left:130px;width:480px;top:122px;text-align:center;font-size:9.5px;line-height:14px;color:var(--muted)">Lorem Ipsum is simply dummy text of the printing and typesetting industry. Lorem Ipsum has been the industry's standard dummy text ever since the 1500s, when an unknown printer took a galley of type and scrambled it to make a type specimen book. It has survived not only five centuries.</p>
    <p class="abs" style="left:0;width:740px;top:187px;text-align:center;font-size:15px;letter-spacing:6px;color:var(--orange)">★★★★★</p>
  </div>
  <svg class="abs" style="left:552px;top:4034px" width="100" height="14" aria-label="Slide indicators"><g fill="#b8d6f7"><circle cx="8" cy="7" r="3"/><circle cx="28" cy="7" r="3"/><circle cx="68" cy="7" r="3"/><circle cx="88" cy="7" r="3"/></g><circle cx="48" cy="7" r="5" fill="#1f8ff2"/></svg>
</section>

<section class="contact-area">
  <div class="abs map" role="img" aria-label="Street map showing the office location"></div>
  <div class="abs footer"></div>
  <div class="abs contact">
    <h3 class="abs" style="left:0;width:384px;top:18px;text-align:center;font-size:20px;color:var(--blue-text);font-weight:500">Get in touch</h3>
    <div class="field" style="top:64px">Name</div>
    <div class="field" style="top:114px">Email Address</div>
    <div class="field" style="top:163px">Contact Num.</div>
    <div class="field" style="top:214px;height:115px">Message</div>
    <a class="btn btn-blue" style="left:141px;top:353px;width:102px;height:22px;font-size:7px">Subscribe</a>
  </div>
</section>

<footer>
  <div class="abs" style="left:510px;top:4548px;display:flex;align-items:center;gap:8px;color:#fff;font-size:17px;font-weight:500"><span style="width:22px;height:22px;border:2px solid #fff;border-radius:50%"></span>LuMora</div>
  <div class="abs" style="left:660px;top:4545px;width:1px;height:76px;background:rgba(255,255,255,.4)"></div>
  <div class="abs f-info">
    <p>✉&nbsp; info@lumora-example.com</p>
    <p>☏&nbsp; +11-555-0142</p>
    <p>⌖&nbsp; Cedar Row 14, Northgate</p>
  </div>
  <div class="abs" style="left:930px;top:4545px;width:1px;height:76px;background:rgba(255,255,255,.4)"></div>
  <span class="social" style="left:996px"></span>
  <span class="social" style="left:1038px"></span>
  <span class="social" style="left:1080px"></span>
  <p class="abs copy">© 2019 All rights reserved. &nbsp;Terms &amp; Conditions | Privacy Policy</p>
</footer>

</body>
</html>
```